Education portal needs a new Email Creative Design

We could not decide on the creative earlier as we were unable to picture how will it look. Hence, we have added content so that we can choose the best design of all. Below is the content to be used for the email creative:
____________________________________
Did you know that 25% of all Americans have experienced at least one divorce?*
41% of first marriages end in divorce!!*

Over 1 million children are affected by divorce each year*

Become a Marriage and Family therapist - Achieve inner-happiness by helping individuals, families and couples resolve their struggles and enhance their lives.
Family Therapists are trained in various modes of therapy in order to prepare them for work with individuals, families, couples, and groups.

With proper training, you will be able to treat:
• Depression and other Affective Disorders
• Childhood Behavioral and Emotional Disorders
• Marital and Relationship Problems
• Conduct Disorder and Delinquency
• Substance Abuse
• Alcoholism
• Domestic Violence
• Severe Mental Illness
• Physical Illness

You could also qualify for financial aid* from the government to pursue this career..

Secure your life by earning upto $78,580* and attain peace of mind while helping others..

__________________________

These are the links to images we liked, but if you have something better, we would love to see them:
http://www.pictovale.example/photo/seperated-50317294?st=7kq2m81
http://www.pictovale.example/photo/domestic-violence-68204937?st=b4n9x52

We are an education portal offering options of schools, colleges, universities and courses to students and working professionals.

We are looking for an email creative which has great call-to-action; be creative and research more if you wish.
Incorporate call-to-action tabs, make it colorful, include pictures and content.
Also attached are industry standard creatives for your reference, let me know if you have any questions.
Updates

Please see new files uploaded

I have uploaded a new creative made by our design team. Follow similar guidelines

For those who have not submitted their designs, please send us soon. Thanks

We thought a content brief will do more justice to this design contest hence we have updated our brief with new content to create a newer design Please submit your designs soon. Thanks

Target Market(s)

25 to 50 years working professionals

Industry/Entity Type

Government

Font styles to use
Serif
Sans Serif
Decorative
Script

Requirements
Must have
• Call-to-action

```html
<!DOCTYPE html>
<html lang="en">
<head>
<meta charset="utf-8">
<title>Scholar Compass – Become a Marriage &amp; Family Therapist</title>
<link href="https://fonts.googleapis.com/css2?family=PT+Sans:wght@400;700&family=Kalam:wght@400&display=swap" rel="stylesheet">
<style>
:root{
  --frame:#1a8fdc;
  --tab:#0f6cb8;
  --tab-active:#3aa7ef;
  --hero:#0d6fba;
  --hero-dark:#0a4f8a;
  --red:#f2534a;
  --red-deep:#d62a1f;
  --fold:#a81d14;
  --btn-red:#ee1c10;
  --btn-blue:#1a78cc;
  --title-blue:#136bb3;
  --link-blue:#1d8ad8;
  --text:#444;
  --row-grey:#f6f6f6;
  --ring:#e4e4e4;
  --thumb-border:#e9e9e9;
  --white:#fff;
}
*{box-sizing:border-box;margin:0;padding:0}
html,body{width:1200px;height:2790px;overflow:hidden;background:var(--white)}
body{position:relative;font-family:"PT Sans",Tahoma,sans-serif;color:var(--text)}

.tab{position:absolute;top:20px;height:50px;border-radius:12px 12px 0 0;background:var(--tab);color:var(--white);font-weight:700;font-size:27px;text-align:center;line-height:44px}
.tab.active{background:var(--tab-active)}
.frame{position:absolute;left:20px;top:68px;width:1160px;height:2712px;background:var(--frame)}
.sheet{position:absolute;left:36px;top:80px;width:1132px;height:2610px;background:var(--white)}

.brand{position:absolute;left:52px;top:102px;display:flex;align-items:center;gap:14px;font-size:40px;font-weight:700;color:var(--red-deep)}
.brand i{display:block;width:30px;height:30px;background:var(--btn-blue)}
.tagline{position:absolute;right:48px;top:106px;font-size:46px;color:var(--red-deep)}
.tagline b{font-weight:700}

.ribbon{position:absolute;left:36px;top:190px;width:1132px;height:110px;background:linear-gradient(#f7685f,var(--red));color:var(--white);padding:12px 0 0 40px}
.ribbon p{font-size:32px;line-height:40px}
.ribbon p.big{font-size:40px;font-weight:700;line-height:46px}
.fold{position:absolute;top:300px}

.hero{position:absolute;left:48px;top:300px;width:1106px;height:412px;background:var(--hero);border-bottom:8px solid var(--hero-dark)}
.hero h1{position:absolute;left:82px;top:92px;width:530px;font-size:54px;line-height:70px;color:var(--white);font-weight:700}
.hero .photo{position:absolute;left:622px;top:16px;width:420px;height:388px;background:radial-gradient(circle at 50% 40%,#6b4a3a,#1c1c1c 70%);border-radius:40% 40% 0 0}

.btn{position:absolute;display:flex;border-radius:10px;overflow:hidden;box-shadow:0 3px 4px rgba(0,0,0,.35)}
.btn .label{background:linear-gradient(#ff4a3c,var(--btn-red) 55%,#c70f05);color:var(--white);display:flex;align-items:center;justify-content:center;white-space:nowrap}
.btn .arrow{background:linear-gradient(#4aa3f0,var(--btn-blue));display:flex;align-items:center;justify-content:center}
.btn-find{left:76px;top:264px;width:432px;height:76px;border:3px solid var(--white)}
.btn-find .label{width:354px;font-family:"Kalam",cursive;font-size:42px}
.btn-find .arrow{width:72px}

.feature{position:absolute;top:774px;width:290px;text-align:center}
.feature .ring{width:188px;height:188px;border-radius:50%;border:2px solid var(--ring);margin:0 auto;display:flex;align-items:center;justify-content:center}
.feature p{margin:38px auto 0;width:260px;font-size:25px;line-height:40px;color:var(--text)}

.section-bar{position:absolute;left:48px;top:1252px;width:1106px;height:84px;background:var(--red);color:var(--white);font-size:33px;text-align:center;line-height:84px}

.row{position:absolute;left:48px;width:1106px}
.row.grey{background:var(--row-grey)}
.thumb{position:absolute;left:32px;width:314px;border:4px solid var(--thumb-border)}
.article h2{position:absolute;left:394px;width:690px;font-size:31px;line-height:46px;font-weight:400;color:var(--title-blue)}
.article p{position:absolute;left:394px;width:690px;font-size:24px;line-height:40px;color:var(--text)}
.btn-more{left:394px;width:212px;height:48px}
.btn-more .label{width:160px;font-size:22px;font-weight:700}
.btn-more .arrow{width:52px}

.more-title{position:absolute;left:0;width:1148px;top:2540px;text-align:center;font-size:31px;font-weight:700;color:var(--link-blue)}
.btn-visit{left:370px;top:2590px;width:430px;height:74px}
.btn-visit .label{width:356px;font-size:38px;font-weight:700}
.btn-visit .arrow{width:74px}

.footer{position:absolute;left:0;width:1200px;top:2714px;text-align:center;color:var(--white);font-size:22px}
</style>
</head>
<body>
<div class="tab active" style="left:40px;width:252px">Career Planning</div>
<div class="tab" style="left:296px;width:268px">Graduate Degrees</div>
<div class="tab" style="left:570px;width:264px">Bachelors Degree</div>
<div class="tab" style="left:842px;width:270px">Popular Degrees</div>
<div class="frame"></div>
<div class="sheet"></div>

<div class="brand"><i></i>Scholar Compass</div>
<div class="tagline">SCHOOL'S in <b>SESSION</b></div>

<div class="ribbon">
  <p>Did you know that 25% of all Americans</p>
  <p class="big">have experienced at least one divorce?*</p>
</div>
<svg class="fold" style="left:36px" width="12" height="16"><polygon points="0,0 12,0 12,16" fill="var(--fold)"/></svg>
<svg class="fold" style="left:1156px" width="12" height="16"><polygon points="0,0 12,0 0,16" fill="var(--fold)"/></svg>

<section class="hero">
  <h1>Become a Marriage<br>&amp; Family Therapist</h1>
  <div class="btn btn-find">
    <span class="label">Find My Program</span>
    <span class="arrow"><svg width="40" height="30" viewBox="0 0 40 30"><path d="M4 3l11 12-11 12M20 3l11 12-11 12" stroke="#fff" stroke-width="6" fill="none"/></svg></span>
  </div>
  <div class="photo" role="img" aria-label="Smiling graduate in a cap and gown holding a diploma"></div>
</section>

<div class="feature" style="left:104px">
  <div class="ring"><svg width="130" height="100" viewBox="0 0 130 100"><polygon points="65,10 125,35 65,60 5,35" fill="var(--title-blue)"/><path d="M30 48v22c20 14 50 14 70 0V48L65 63z" fill="var(--title-blue)"/><path d="M18 40v40" stroke="var(--title-blue)" stroke-width="4"/><rect x="12" y="78" width="12" height="14" fill="var(--title-blue)"/></svg></div>
  <p>41% of first marriages end in divorce! Trained therapists help couples heal.*</p>
</div>
<div class="feature" style="left:456px">
  <div class="ring"><svg width="70" height="110" viewBox="0 0 70 110"><path d="M35 4a31 31 0 0 1 18 56c-4 4-6 8-6 14H23c0-6-2-10-6-14A31 31 0 0 1 35 4z" fill="var(--title-blue)"/><rect x="22" y="80" width="26" height="7" fill="var(--title-blue)"/><rect x="22" y="91" width="26" height="7" fill="var(--title-blue)"/><rect x="28" y="101" width="14" height="6" fill="var(--title-blue)"/></svg></div>
  <p>Over 1 million children are affected by divorce each year*</p>
</div>
<div class="feature" style="left:776px">
  <div class="ring"><svg width="100" height="90" viewBox="0 0 100 90"><polyline points="10,80 35,32 58,50 88,12" stroke="var(--title-blue)" stroke-width="4" fill="none"/><g fill="var(--title-blue)"><circle cx="10" cy="80" r="8"/><circle cx="35" cy="32" r="8"/><circle cx="58" cy="50" r="8"/><circle cx="88" cy="12" r="8"/></g></svg></div>
  <p>Secure your life by earning up to $78,580* while helping others</p>
</div>

<div class="section-bar">Why Become a Marriage and Family Therapist?</div>

<article class="row article" style="top:1360px;height:250px">
  <div class="thumb" role="img" aria-label="Couple sitting apart after a separation" style="top:20px;height:210px;background:linear-gradient(90deg,#8a7a6a,#c9b5a0 50%,#6a5a4e)"></div>
  <h2 style="top:26px">Achieve Inner-Happiness by Helping Others</h2>
  <p style="top:76px">Help individuals, families and couples resolve their struggles and enhance their lives.</p>
  <div class="btn btn-more" style="top:170px"><span class="label">Read More</span><span class="arrow"><svg width="28" height="22" viewBox="0 0 40 30"><path d="M4 3l11 12-11 12M20 3l11 12-11 12" stroke="#fff" stroke-width="6" fill="none"/></svg></span></div>
</article>

<article class="row grey article" style="top:1616px;height:268px">
  <div class="thumb" role="img" aria-label="Therapist listening to a family in a counselling session" style="top:28px;height:210px;background:linear-gradient(90deg,#e8e2da,#c9b19a 45%,#9a9a9a)"></div>
  <h2 style="top:34px">Trained in Various Modes of Therapy</h2>
  <p style="top:84px">Prepare for work with individuals, families, couples and groups in many settings.</p>
  <div class="btn btn-more" style="top:178px"><span class="label">Read More</span><span class="arrow"><svg width="28" height="22" viewBox="0 0 40 30"><path d="M4 3l11 12-11 12M20 3l11 12-11 12" stroke="#fff" stroke-width="6" fill="none"/></svg></span></div>
</article>

<article class="row article" style="top:1884px;height:316px">
  <div class="thumb" role="img" aria-label="Distressed person in a dim room, representing domestic violence" style="top:38px;height:206px;background:linear-gradient(90deg,#3e3a40,#6e6470 45%,#a89a96)"></div>
  <h2 style="top:44px">Treat Depression, Behavioral and Relationship Problems</h2>
  <p style="top:136px">Also conduct disorder, substance abuse, alcoholism, domestic violence and severe illness.</p>
  <div class="btn btn-more" style="top:236px"><span class="label">Read More</span><span class="arrow"><svg width="28" height="22" viewBox="0 0 40 30"><path d="M4 3l11 12-11 12M20 3l11 12-11 12" stroke="#fff" stroke-width="6" fill="none"/></svg></span></div>
</article>

<article class="row grey article" style="top:2200px;height:310px">
  <div class="thumb" role="img" aria-label="Smiling working professional studying in front of a bookshelf" style="top:34px;height:204px;background:linear-gradient(90deg,#d8c8b0,#6a4a3a 45%,#c9b59a)"></div>
  <h2 style="top:40px">Qualify for Government Financial Aid* to Pursue This Career</h2>
  <p style="top:134px">Earn up to $78,580* and attain peace of mind while helping others live better lives.</p>
  <div class="btn btn-more" style="top:240px"><span class="label">Read More</span><span class="arrow"><svg width="28" height="22" viewBox="0 0 40 30"><path d="M4 3l11 12-11 12M20 3l11 12-11 12" stroke="#fff" stroke-width="6" fill="none"/></svg></span></div>
</article>

<div class="more-title">Find Out More</div>
<div class="btn btn-visit"><span class="label">Visit Our Website</span><span class="arrow"><svg width="40" height="30" viewBox="0 0 40 30"><path d="M4 3l11 12-11 12M20 3l11 12-11 12" stroke="#fff" stroke-width="6" fill="none"/></svg></span></div>

<div class="footer">All rights reserved, Scholar Compass</div>
</body>
</html>
```